Fine Dining Restaurant needs Harbour Stakes Day Flyer

We need a flyer to promote Harbour Stakes day at our restaurant in Port Ellery, QLD.
Details:
6th November 2018
It's a ticketed event, including a fine-dining 4 course lunch, with 3 hour drinks package, to include sweeps & prizes.
Starts 11:30 - 14:30.
Ticket price: $160 with $5 from each ticket going to Tails & Whiskers
Cash bar also available.
Address: 47 Copperleaf Lane, Port Ellery
Contact: 0740553819 or bookings@lorindas.net.au
*Big screen TV's
*Sweeps
*Best Dressed prizes and more...
*Glass of sparkling wine on arrival
*Discount for tables of 8 or more...
Design: we'd like to see a really elegant design for the flyer, with the use of tropical florals, utilising whites and some burnt orange colours if suitable.
Size: To be printed on A4

```html
<!DOCTYPE html>
<html lang="en">
<head>
<meta charset="utf-8">
<title>Harbour Stakes Day Flyer</title>
<link href="https://fonts.googleapis.com/css2?family=Great+Vibes&family=Oswald:wght@500&family=Open+Sans:wght@400;600;700&display=swap" rel="stylesheet">
<style>
  :root{
    --paper:#ffffff;
    --ink:#2b2b2b;
    --muted:#555555;
    --orange:#e0782a;
    --orange-light:#f4b27a;
    --grey-band:#e9e9e9;
    --floral-green:#a9c298;
    --floral-pink:#f5d3d3;
    --splash:#c9c9d6;
  }
  *{margin:0;padding:0;box-sizing:border-box}
  html,body{width:707px;height:1200px;overflow:hidden;background:var(--paper)}
  .flyer{position:relative;width:707px;height:1200px;background:var(--paper);font-family:"Open Sans",sans-serif;color:var(--ink);text-align:center}
  .floral{position:absolute;top:0;width:220px;height:115px;opacity:.8}
  .floral--left{left:0;border-bottom-right-radius:115px;background:radial-gradient(circle at 30% 30%,var(--floral-pink),var(--floral-green) 75%)}
  .floral--right{right:0;border-bottom-left-radius:115px;background:radial-gradient(circle at 70% 30%,var(--floral-pink),var(--floral-green) 75%)}
  .brand{position:absolute;top:58px;left:0;right:0;display:flex;justify-content:center;align-items:center}
  .brand__name{font-family:"Open Sans",sans-serif;font-weight:600;font-size:30px;letter-spacing:2px;color:var(--ink)}
  .title{position:absolute;top:130px;left:0;right:0;font-family:"Great Vibes",cursive;font-weight:400;font-size:70px;color:var(--orange);line-height:1}
  .hero{position:absolute;top:250px;left:110px;width:490px;height:400px;border-radius:40% 55% 45% 50%;background:radial-gradient(ellipse at 55% 45%,#b5652e 0%,#8a4a2a 35%,var(--splash) 65%,rgba(255,255,255,0) 80%)}
  .date{position:absolute;top:672px;left:0;right:0;font-family:"Oswald",sans-serif;font-weight:500;font-size:30px;color:var(--orange)}
  .details{position:absolute;top:724px;left:150px;right:150px;font-size:14px;line-height:1.45;color:var(--muted)}
  .ticket{position:absolute;top:800px;left:0;right:0}
  .ticket__label{font-weight:700;font-size:17px;color:var(--orange)}
  .ticket__price{font-size:15px;font-weight:600;margin-top:4px}
  .cashbar{position:absolute;top:862px;left:0;width:707px;height:46px;background:linear-gradient(90deg,var(--orange-light) 0%,rgba(244,178,122,.4) 45%,rgba(255,255,255,0) 75%)}
  .cashbar__text{font-weight:700;font-size:20px;line-height:46px}
  .contact{position:absolute;top:930px;left:0;right:0;list-style:none;font-size:15px;font-weight:600}
  .contact li{display:flex;justify-content:center;align-items:center;gap:8px;height:34px}
  .contact svg{width:16px;height:16px;fill:var(--orange)}
  .extras{position:absolute;top:1060px;left:0;width:707px;height:90px;background:var(--grey-band);padding:18px 90px;font-size:14px;line-height:1.5;color:var(--muted)}
  .stripe{position:absolute;bottom:0;left:0;width:707px;height:50px}
</style>
</head>
<body>
<main class="flyer">
  <div class="floral floral--left" role="img" aria-label="Tropical florals with pink blooms and green leaves"></div>
  <div class="floral floral--right" role="img" aria-label="Tropical florals with pink blooms and green leaves"></div>

  <header class="brand">
    <span class="brand__name">Lorinda's</span>
  </header>

  <h1 class="title">Harbour Stakes Day</h1>

  <div class="hero" role="img" aria-label="Watercolour racehorse with jockey galloping over a grey-blue paint splash"></div>

  <p class="date">6th November 2018 | Starts - 11:30 - 14:30</p>

  <p class="details">It's A Ticketed Event, Including A Fine-dining 4 Course Lunch, With 3 Hour Drinks Package, To Include Sweeps &amp; Prizes</p>

  <section class="ticket">
    <p class="ticket__label">Ticket price</p>
    <p class="ticket__price">$160 with $5 from each ticket going to Tails &amp; Whiskers</p>
  </section>

  <div class="cashbar"><p class="cashbar__text">Cash bar also available</p></div>

  <ul class="contact">
    <li><svg viewBox="0 0 24 24"><path d="M12 2a7 7 0 0 0-7 7c0 5 7 13 7 13s7-8 7-13a7 7 0 0 0-7-7zm0 9.5A2.5 2.5 0 1 1 12 6.5a2.5 2.5 0 0 1 0 5z"/></svg>47 Copperleaf Lane, Port Ellery</li>
    <li><svg viewBox="0 0 24 24"><path d="M6.6 10.8a15 15 0 0 0 6.6 6.6l2.2-2.2a1 1 0 0 1 1-.25 11.4 11.4 0 0 0 3.6.6 1 1 0 0 1 1 1V20a1 1 0 0 1-1 1A17 17 0 0 1 3 4a1 1 0 0 1 1-1h3.5a1 1 0 0 1 1 1c0 1.25.2 2.45.6 3.6a1 1 0 0 1-.25 1z"/></svg>0740553819</li>
    <li><svg viewBox="0 0 24 24"><path d="M3 5h18v14H3zm2 2v.5l7 4.5 7-4.5V7zm0 2.8V17h14V9.8l-7 4.5z"/></svg>bookings@lorindas.net.au</li>
  </ul>

  <section class="extras">
    <p>Big screen TV's | Sweeps | Best Dressed prizes and more...</p>
    <p>Glass of sparkling wine on arrival | Discount for tables of 8 or more...</p>
  </section>

  <svg class="stripe" viewBox="0 0 707 50" preserveAspectRatio="none" aria-hidden="true">
    <polygon points="0,20 420,20 400,50 0,50" fill="var(--orange)"/>
    <polygon points="430,20 707,20 707,50 410,50" fill="var(--orange-light)"/>
  </svg>
</main>
</body>
</html>
```